Fox & Fig honey company needs a label design.

We need a label design for a new honey company, based in the state of Florida called 'Fox & Fig". We are supplying our online customers with the highest quality of the various kinds of raw honey. Our product is honey in the oval hexagon glass jar with black lid. We would like to see designs that use black background with gold font .
In the upper part of the label is gold flying Honey Bee (profile, silhouette). The name of the brand "Fox & Fig" - Caramel font. Additional fonts are Cinzel, Source Sans Pro. Label measurements 2.6" by 3".
Label content:
Fox & Fig
RAW HONEY
wildflower
PURE & NATURAL
made by Florida Bees
foxandfigjars.com
NET WT 12oz (340g)

The final design should have eye catching, luxurious look.
Updates

Need extra days to review

Target Market(s)

Luxury

Industry/Entity Type

Food (bee products)

Font styles to use
Other font styles liked:
• caramel

Colors

Designer to choose colors to be used in the design.

Requirements
Must have
• Gold letters on black background, Drawing of a bee, flying in profile

```html
<!DOCTYPE html>
<html lang="en">
<head>
<meta charset="utf-8">
<title>Fox &amp; Fig Raw Honey Label</title>
<link href="https://fonts.googleapis.com/css2?family=Caramel&family=Source+Sans+3:wght@400;500&display=swap" rel="stylesheet">
<style>
  :root {
    --paper: #ffffff;
    --label-black: #000000;
    --gold-light: #f3d27a;
    --gold-mid: #d4a23a;
    --gold-deep: #8a5a14;
    --gold-gradient: linear-gradient(180deg, #f6d98a 0%, #d9a640 45%, #a8711c 75%, #e0b45a 100%);
  }
  html, body {
    margin: 0;
    padding: 0;
    width: 1061px;
    height: 1200px;
    overflow: hidden;
    background: var(--paper);
  }
  .canvas {
    position: relative;
    width: 1061px;
    height: 1200px;
    background: var(--paper);
  }
  .label {
    position: absolute;
    left: 47px;
    top: 40px;
    width: 967px;
    height: 1125px;
    background: var(--label-black);
    overflow: hidden;
  }
  .honeycomb-glow {
    position: absolute;
    inset: 0;
    background:
      radial-gradient(ellipse 300px 240px at 100% 0%, rgba(212,162,58,0.35), transparent 70%),
      radial-gradient(ellipse 260px 200px at 0% 0%, rgba(138,90,20,0.3), transparent 70%),
      radial-gradient(ellipse 200px 380px at 100% 55%, rgba(138,90,20,0.28), transparent 70%),
      radial-gradient(ellipse 160px 300px at 0% 60%, rgba(138,90,20,0.25), transparent 70%),
      radial-gradient(ellipse 300px 180px at 10% 100%, rgba(212,162,58,0.35), transparent 70%),
      radial-gradient(ellipse 300px 180px at 95% 100%, rgba(212,162,58,0.3), transparent 70%);
  }
  .gold-text {
    position: absolute;
    left: 0;
    width: 100%;
    text-align: center;
    margin: 0;
    background: var(--gold-gradient);
    -webkit-background-clip: text;
    background-clip: text;
    color: transparent;
    font-family: "Source Sans 3", "Source Sans Pro", sans-serif;
    font-weight: 400;
    line-height: 1;
  }
  .bee-emblem {
    position: absolute;
    left: 434px;
    top: 75px;
    width: 161px;
    height: 160px;
  }
  .brand-name {
    top: 250px;
    font-family: "Caramel", cursive;
    font-size: 170px;
    line-height: 1.1;
    padding: 0 20px;
    box-sizing: border-box;
  }
  .product-type {
    top: 510px;
    font-size: 62px;
    letter-spacing: 6px;
  }
  .variety {
    top: 617px;
    font-size: 50px;
  }
  .claim {
    top: 735px;
    font-size: 76px;
    letter-spacing: 1px;
  }
  .website {
    top: 865px;
    font-size: 40px;
  }
  .footnote {
    position: absolute;
    top: 1022px;
    margin: 0;
    font-family: "Source Sans 3", "Source Sans Pro", sans-serif;
    font-size: 28px;
    color: var(--gold-mid);
    line-height: 1;
  }
  .net-weight { left: 68px; }
  .origin { right: 63px; }
</style>
</head>
<body>
<div class="canvas">
  <section class="label">
    <div class="honeycomb-glow" role="img" aria-label="Faint gold honeycomb pattern framing the label edges"></div>

    <svg class="bee-emblem" viewBox="0 0 161 160" role="img" aria-label="Gold flying honey bee in profile">
      <defs>
        <radialGradient id="beeGold" cx="50%" cy="45%" r="60%">
          <stop offset="0%" stop-color="#e9bf5e"/>
          <stop offset="100%" stop-color="#8a5a14"/>
        </radialGradient>
      </defs>
      <ellipse cx="80" cy="80" rx="70" ry="68" fill="url(#beeGold)" opacity="0.55"/>
    </svg>

    <h1 class="gold-text brand-name">Fox &amp; Fig</h1>
    <p class="gold-text product-type">RAW HONEY</p>
    <p class="gold-text variety">wildflower</p>
    <p class="gold-text claim">PURE &amp; NATURAL</p>
    <p class="gold-text website">foxandfigjars.com</p>

    <p class="footnote net-weight">NET WT 12oz (340g)</p>
    <p class="footnote origin">Made by Florida Bees</p>
  </section>
</div>
</body>
</html>
```